Wren Vehicle Polishing (Mobile detail)

I need a business card made up. I'd like it to be different in some form, either raised, embossed, debossed, something cool that stands out. (preferably embossed text somewhere in it). I will be including the Initial png file. Let me know if you need the photoshop of adobe illustrator file to work with.

Information to be included: Text: XXX-XXX-XXXX Phone: XXX-XXX-XXXX Email: wrenpolishcrew@mailbox-demo.net Website: www.socialpage-demo.net/wrenpolishKTR Hours of operation: Mon - Fri 7:00AM to 8:00PM Sat - 10:00AM to 8:00PM

Target Market(s)

Mobile automotive detailing

Industry/Entity Type

Automotive

Contact Information for Business Card

Make it stand out with embossed lettering, I'd also like the background to be glossy black or matte, something that represents a shiny car, black preferred

Requirements
Must have
• A glossy background, or something.
• My logo, pick one of them that best fits your design.
Should not have
• White background,
• something that does not stand out.

```html
<!DOCTYPE html>
<html lang="en">
<head>
<meta charset="utf-8">
<title>Wren Vehicle Polishing – Business Card</title>
<link rel="stylesheet" href="https://fonts.googleapis.com/css2?family=Open+Sans:wght@400;600;700&display=swap">
<style>
  :root {
    --bg: #e9e6e3;
    --card-black: #000000;
    --orange: #f26a21;
    --orange-deep: #e4571a;
    --silver: #c9c9c9;
    --silver-light: #f2f2f2;
    --yellow: #fbf06b;
    --white: #ffffff;
  }
  * { margin: 0; padding: 0; box-sizing: border-box; }
  html, body { width: 1200px; height: 900px; overflow: hidden; }
  body {
    background: var(--bg);
    font-family: "Open Sans", Arial, sans-serif;
    position: relative;
  }
  .card {
    position: absolute;
    background: var(--card-black);
    overflow: hidden;
    box-shadow: 0 6px 18px rgba(0,0,0,0.25);
  }
  .card-front { left: 77px; top: 35px; width: 588px; height: 362px; }
  .card-back  { left: 388px; top: 505px; width: 565px; height: 352px; }
  .bands { position: absolute; left: 0; top: 0; width: 100%; height: 100%; }

  .brand {
    position: absolute;
    left: 50px; top: 92px;
    width: 200px;
    display: flex; align-items: center; gap: 12px;
    color: var(--silver);
    font-weight: 700;
    font-size: 24px;
    line-height: 1.15;
  }
  .brand-dot {
    flex: none;
    width: 22px; height: 22px;
    border-radius: 50%;
    background: var(--orange);
  }

  .person { position: absolute; left: 283px; top: 58px; }
  .person-name { color: var(--orange); font-weight: 600; font-size: 20px; line-height: 1.2; }
  .person-title { color: var(--white); font-size: 15px; margin-top: 2px; }

  .contacts { position: absolute; left: 283px; top: 194px; list-style: none; }
  .contacts li {
    display: flex; align-items: center; gap: 9px;
    color: var(--white); font-size: 15px; height: 25px;
    white-space: nowrap;
  }
  .contacts svg { width: 12px; height: 12px; fill: var(--orange); }

  .web {
    position: absolute; left: 280px; top: 314px;
    color: var(--white); font-weight: 700; font-size: 13px;
    letter-spacing: -0.2px;
    white-space: nowrap;
  }

  .back-name {
    position: absolute; left: 70px; top: 112px;
    color: var(--silver); font-weight: 700; font-size: 38px;
    white-space: nowrap;
  }
  .hours-title {
    position: absolute; left: 283px; top: 224px;
    color: var(--white); font-weight: 700; font-size: 20px;
    white-space: nowrap;
  }
  .hours {
    position: absolute; left: 283px; top: 280px;
    color: var(--white); font-weight: 700; font-size: 16px; line-height: 24px;
    white-space: nowrap;
  }
  .hours span { font-weight: 400; }
</style>
</head>
<body>

<section class="card card-front">
  <svg class="bands" viewBox="0 0 588 362" aria-hidden="true">
    <defs>
      <linearGradient id="silverBand" x1="0" y1="0" x2="0" y2="1">
        <stop offset="0" stop-color="#ffffff"/>
        <stop offset="1" stop-color="#9c9c9c"/>
      </linearGradient>
      <linearGradient id="orangeBand" x1="0" y1="0" x2="0" y2="1">
        <stop offset="0" stop-color="#f47b2a"/>
        <stop offset="1" stop-color="#e4571a"/>
      </linearGradient>
    </defs>
    <polygon points="0,311 268,311 246,337 0,337" fill="url(#silverBand)"/>
    <polygon points="270,303 588,303 588,362 0,362 0,340 248,340" fill="url(#orangeBand)"/>
  </svg>

  <div class="brand">
    <span class="brand-dot"></span>
    <span>Wren Vehicle Polishing</span>
  </div>

  <div class="person">
    <p class="person-name">Dorian Keller</p>
    <p class="person-title">Managing Director</p>
  </div>

  <ul class="contacts">
    <li><svg viewBox="0 0 12 12"><path d="M2.5 0.5l2 2.2-1 1.3c.7 1.5 1.9 2.8 3.5 3.6l1.3-1 2.2 2-1.3 2.1C5.2 10.5 1.4 6.8 0.5 1.8z"/></svg>XXX-XXX-XXXX</li>
    <li><svg viewBox="0 0 12 12"><path d="M3 0h6v12H3zM4.2 1.2v8.4h3.6V1.2z"/></svg>XXX-XXX-XXXX</li>
    <li><svg viewBox="0 0 12 12"><path d="M0 2h12v8H0zM1 3l5 3.5L11 3v-.2H1z"/></svg>wrenpolishcrew@mailbox-demo.net</li>
  </ul>

  <p class="web">www.socialpage-demo.net/wrenpolishKTR</p>
</section>

<section class="card card-back">
  <svg class="bands" viewBox="0 0 565 352" aria-hidden="true">
    <defs>
      <linearGradient id="orangeBack" x1="0" y1="0" x2="0" y2="1">
        <stop offset="0" stop-color="#f47b2a"/>
        <stop offset="1" stop-color="#e4571a"/>
      </linearGradient>
    </defs>
    <polygon points="0,272 250,272 228,296 0,296" fill="var(--yellow)"/>
    <polygon points="258,263 565,263 565,352 0,352 0,298 230,298" fill="url(#orangeBack)"/>
  </svg>

  <p class="back-name">Wren Vehicle Polishing</p>
  <p class="hours-title">KTR Hours of operation</p>
  <p class="hours">Mon - Fri: <span>7:00AM to 8:00PM</span><br>Sat: <span>10:00AM to 8:00PM</span></p>
</section>

</body>
</html>
```